Granite Civic Builders Summit (GCBS) needs a flyer and logo design

We need a save the date flyer that can be easily edited to be a header only with event title, date and location.
We also are looking for a conference logo that will go well with our company logo.
Updates
Most of you are submitting an agenda design. Not a graphic flyer design. This isn't what I'm needing. I need something that can easily be a save the date with a header and is graphically appealing. Additionally, I've only gotten 2 logo designs.
Low design quality
Target Market(s)
Architects, engineers, public owners, contractors, attorneys
Industry/Entity Type
Construction
Logo Text
Granite Civic Builder's Summit
Requirements
Must have
- Flyer should Have:
- Title: "A Lantern Across Stormy Seas - Project Delivery to Operations”
- Date: August 8-9, 2019
- Location: Fort Worth, TX
- One-page only
- Conference Logo should be relatable to our company logo: Granite Civic Builders Summit.
Nice to have
- Topics:
- Alternative Constrcting: JOC & Design-Build
- Dealing with Contracting in a Tight TX Industry
- Tools & Technologies Project Delivery and Operations: Design and Construction
- Tools & Technologies: Coordinating Operations
Should not have
- Detailed agenda

```html
<!DOCTYPE html>
<html lang="en">
<head>
<meta charset="utf-8">
<title>Granite Civic Builders Summit – Save the Date</title>
<link rel="stylesheet" href="https://fonts.googleapis.com/css2?family=Alfa+Slab+One&family=Montserrat:wght@600;700;800&family=Lato:ital,wght@0,400;0,700;1,700&display=swap">
<style>
  :root{
    --ink:#1f1f1f;
    --night:#0d140f;
    --glow:#3f5c2c;
    --green:#8cc63f;
    --navy:#1d3f8f;
    --band:#1f4496;
    --tab:#4c4d4f;
    --tab-dark:#2f3031;
    --mist:#e9eaec;
    --paper:#ffffff;
  }
  *{margin:0;padding:0;box-sizing:border-box}
  html,body{width:900px;height:1200px;overflow:hidden;background:var(--paper)}
  .flyer{position:relative;width:900px;height:1200px;overflow:hidden;font-family:"Lato",sans-serif;color:var(--ink)}

  .hero{position:absolute;left:0;top:0;width:900px;height:530px;
    background:radial-gradient(ellipse 70% 55% at 50% 30%,var(--glow) 0%,#1c2a19 55%,var(--night) 100%)}
  .event-name{position:absolute;left:43px;top:47px;width:817px;height:67px;border:4px solid var(--paper);
    display:flex;align-items:center;justify-content:center;
    font-family:"Alfa Slab One",serif;font-size:31px;color:var(--paper);letter-spacing:.5px;white-space:nowrap}
  .headline{position:absolute;left:0;top:146px;width:900px;text-align:center;
    font-family:"Montserrat",sans-serif;font-weight:800;font-size:50px;line-height:53px;color:var(--paper);letter-spacing:-1.5px;white-space:nowrap}
  .where-when{position:absolute;left:0;top:327px;width:900px;display:flex;justify-content:center;align-items:center;gap:10px;
    font-family:"Alfa Slab One",serif;font-size:29px;color:var(--paper)}
  .where-when .date{background:var(--green);color:var(--ink);padding:4px 16px;line-height:34px}

  .divider{position:absolute;left:0;top:400px}
  .lower{position:absolute;left:0;top:520px;width:900px;height:680px}
  .lower .left{position:absolute;left:0;top:0;width:453px;height:100%;background:var(--paper)}
  .lower .right{position:absolute;left:453px;top:0;width:447px;height:100%;background:var(--mist)}
  .section-tab{position:absolute;left:318px;top:443px;width:267px;height:63px;background:var(--tab);
    display:flex;align-items:center;justify-content:center;white-space:nowrap;
    font-family:"Alfa Slab One",serif;font-size:28px;color:var(--paper);letter-spacing:1px}

  .day{position:absolute;top:538px}
  .day.thursday{left:0;width:453px;padding:0 36px 0 40px}
  .day.friday{left:453px;width:447px;padding:0 36px 0 40px}
  .day-title{font-family:"Montserrat",sans-serif;font-weight:700;font-size:23px;line-height:29px;color:var(--navy);text-align:center;letter-spacing:-.3px}
  .day-hours{font-family:"Montserrat",sans-serif;font-weight:600;font-size:15px;line-height:20px;color:var(--ink);text-align:center;margin-top:6px;margin-bottom:34px}
  .topic{padding-left:16px;border-left:4px solid var(--green);margin-bottom:34px}
  .topic .label{display:block;font-family:"Montserrat",sans-serif;font-weight:700;font-size:14px;line-height:18px;color:var(--navy);letter-spacing:1px;margin-bottom:6px}
  .topic .title{font-weight:700;font-style:italic;font-size:20px;line-height:26px;color:var(--ink)}

  .footer{position:absolute;left:0;top:1040px}
  .org{position:absolute;left:512px;top:1086px;display:flex;align-items:center;gap:14px}
  .org .mark{width:86px;height:86px;border-radius:50%;background:var(--paper)}
  .org .name{font-family:"Montserrat",sans-serif;font-weight:600;font-size:23px;line-height:27px;color:var(--paper)}
</style>
</head>
<body>
<main class="flyer">
  <div class="hero" role="img" aria-label="Photograph of a conference audience facing a brightly lit stage, tinted dark green"></div>

  <div class="event-name">GRANITE CIVIC BUILDERS SUMMIT</div>
  <h1 class="headline">A LANTERN ACROSS<br>STORMY SEAS PROJECT<br>DELIVERY TO OPERATIONS</h1>
  <div class="where-when"><span>FT. WORTH, TEXAS</span><span class="date">AUGUST 8-9, 2019</span></div>

  <svg class="divider" width="900" height="130" viewBox="0 400 900 130" aria-hidden="true">
    <defs>
      <linearGradient id="split" x1="0" y1="0" x2="900" y2="0" gradientUnits="userSpaceOnUse">
        <stop offset="0.503" stop-color="#ffffff"/>
        <stop offset="0.503" stop-color="#e9eaec"/>
      </linearGradient>
    </defs>
    <path d="M0,520 C230,400 670,400 900,520 L900,530 L0,530 Z" fill="#8cc63f"/>
    <path d="M0,530 C250,420 650,420 900,530 Z" fill="url(#split)"/>
    <polygon points="270,443 318,443 318,506" fill="#2f3031"/>
    <polygon points="630,443 585,443 585,506" fill="#2f3031"/>
  </svg>

  <div class="lower"><div class="left"></div><div class="right"></div></div>
  <div class="section-tab">SAVE THE DATE</div>

  <section class="day thursday">
    <h2 class="day-title">THURSDAY, AUGUST 8TH</h2>
    <p class="day-hours">11:30 A.M. – 5:00 P.M.</p>
    <div class="topic">
      <span class="label">TOPIC 1</span>
      <p class="title">Alternative Contracting: JOC and Design-Build Deliveries</p>
    </div>
    <div class="topic">
      <span class="label">TOPIC 2</span>
      <p class="title">Dealing with Contracting in a Tight Texas Industry</p>
    </div>
  </section>

  <section class="day friday">
    <h2 class="day-title">FRIDAY, AUGUST 9TH</h2>
    <p class="day-hours">7:30 A.M. – 12:30 P.M.</p>
    <div class="topic">
      <span class="label">TOPIC 3A</span>
      <p class="title">Tools and Technologies from Project Delivery into Operations: Design and Construction</p>
    </div>
    <div class="topic">
      <span class="label">TOPIC 3B</span>
      <p class="title">Tools and Technologies: Coordinating Operations</p>
    </div>
  </section>

  <svg class="footer" width="900" height="160" viewBox="0 1040 900 160" aria-hidden="true">
    <path d="M395,1200 C420,1110 470,1060 560,1057 L900,1057 L900,1200 Z" fill="#1f4496"/>
    <rect x="0" y="1167" width="900" height="33" fill="#1f4496"/>
  </svg>

  <div class="org">
    <span class="mark"></span>
    <span class="name">Keystone Works<br>Institute</span>
  </div>
</main>
</body>
</html>
```